I am a health and wellness guru. I am looking to make a website. Nothing too extensive but something to just promote on my socials and sell the info I know as digital assets. I will sell my daily workout as a monthly payment, and they will get updates on what I do daily... As well as a pdf of my day and a guide to a healthy lifestyle. I may offer meal plans and coaching as well. It will be called a venture brightpath and then offer those things. my Instagram @marlon_tibbet you can see kinda my vibe off stuff. I want a clean aesthetic look and simple. Whatever photos you reccoment ill provide when I pick a winning design

Target Market(s)

people who want to buy access to my way of life

Coding

Font styles to use
Serif
Sans Serif

Requirements
Must have
• Venture Brightpath by Marlon Tibbet
Nice to have
• About, plans to buy, why health and wellness is important. (exsposure to subnlight, ice baht, sauna, daily movement, whole foods)

```html
<!DOCTYPE html>
<html lang="en">
<head>
<meta charset="utf-8">
<title>Venture Brightpath by Marlon Tibbet</title>
<link href="https://fonts.googleapis.com/css2?family=Roboto:wght@400;500;700&family=Allura&display=swap" rel="stylesheet">
<style>
:root{
  --green:#4cc69f;
  --red:#d9473a;
  --ink:#222222;
  --body:#555555;
  --pale:#eef4f4;
  --white:#ffffff;
  --line:#e3e8e8;
}
*{box-sizing:border-box;margin:0;padding:0}
html,body{width:1200px;height:4209px;overflow:hidden}
body{font-family:'Roboto',sans-serif;color:var(--ink);background:var(--white);position:relative}
section,header,footer{position:absolute;left:0;width:1200px}
.abs{position:absolute}
.script{font-family:'Allura',cursive;font-weight:400}
.btn{position:absolute;display:flex;align-items:center;justify-content:center;background:var(--green);color:var(--white);font-weight:500;font-size:17px;letter-spacing:.5px;border-radius:30px;text-transform:uppercase}
.para{position:absolute;font-size:15px;line-height:28px;color:var(--body)}
.h2{position:absolute;font-weight:700;font-size:44px;letter-spacing:1px;text-transform:uppercase;color:var(--ink)}

/* hero */
.hero{top:0;height:638px;background:linear-gradient(90deg,#6b1f22 0%,#3a1c1e 35%,#1c1c1e 70%,#161617 100%)}
.hero-photo{position:absolute;left:430px;top:0;width:770px;height:638px;background:radial-gradient(ellipse at 40% 35%,rgba(120,110,105,.55),rgba(20,20,22,0) 60%)}
.brand{position:absolute;color:var(--white);font-weight:500;line-height:1}
.brand .name{font-size:23px;letter-spacing:2px}
.brand .by{font-size:16px;margin-top:10px;margin-left:135px;letter-spacing:1px}
.nav{position:absolute;top:67px;left:548px;display:flex;gap:38px;color:var(--white);font-size:16px;font-weight:500}
.account{position:absolute;top:13px;left:942px;color:var(--white);font-size:15px;display:flex;align-items:center;gap:7px}
.hero .script{position:absolute;left:108px;top:158px;font-size:64px;color:var(--white)}
.hero h1{position:absolute;left:108px;top:248px;font-size:52px;line-height:62px;font-weight:700;color:var(--white);letter-spacing:1px}

/* about */
.about{top:638px;height:652px;background:var(--white)}
.about-glow{position:absolute;left:330px;top:40px;width:260px;height:560px;background:radial-gradient(ellipse at center,rgba(217,71,58,.35),rgba(217,71,58,0) 70%)}
.about-photo{position:absolute;left:111px;top:88px;width:355px;height:457px;border-radius:10px;background:linear-gradient(180deg,#4d6f94 0%,#7a8ea3 45%,#8a7a6e 75%,#9a8878 100%)}
.about-word{position:absolute;left:438px;top:110px;width:60px;font-size:74px;font-weight:700;color:var(--white);line-height:84px;text-align:center;text-shadow:0 0 2px #444,0 0 0 #444;-webkit-text-stroke:2px #222}
.about .script{position:absolute;left:578px;top:80px;font-size:52px}
.about h2{position:absolute;left:634px;top:140px;font-size:40px;font-weight:700;letter-spacing:1px}

/* courses */
.courses{top:1290px;height:985px;background:var(--pale)}
.courses .script{position:absolute;left:0;width:1200px;text-align:center;top:55px;font-size:56px}
.cards{position:absolute;top:238px;left:127px;width:946px;height:155px}
.connector{position:absolute;top:77px;left:75px;width:796px;border-top:2px dashed #9fcfcf}
.card{position:absolute;top:0;width:150px;height:155px;background:var(--white);border-radius:6px;box-shadow:0 4px 14px rgba(0,0,0,.05);display:flex;flex-direction:column;align-items:center;justify-content:flex-end;padding-bottom:18px;font-size:19px;line-height:23px;text-align:center;color:var(--ink)}
.card svg{position:absolute;top:14px;left:43px}
.card.active{background:var(--red);color:var(--white)}
.plan-title{position:absolute;left:111px;top:478px;font-size:29px;font-weight:500}
.shot{position:absolute;border-radius:6px}
.shot-glow{position:absolute;left:560px;top:520px;width:600px;height:420px;background:radial-gradient(ellipse at center,rgba(217,71,58,.18),rgba(217,71,58,0) 65%)}

/* benefits */
.benefits{top:2275px;height:823px;background:var(--white)}
.benefit-photo{position:absolute;left:0;top:163px;width:505px;height:517px;border-radius:0 260px 260px 0;background:linear-gradient(135deg,#4e5a36 0%,#76804e 35%,#a7b2b8 60%,#5b6068 100%)}
.benefits .script{position:absolute;left:570px;top:65px;font-size:56px}
.benefits .h2{left:573px;top:128px;line-height:63px;font-size:46px}
.acc{position:absolute;left:573px;width:515px;height:50px;border-radius:25px;background:var(--pale);display:flex;align-items:center;justify-content:space-between;padding:0 30px 0 33px;font-size:19px;font-weight:500}
.acc.open{background:var(--red);color:var(--white)}

/* guide */
.guide{top:3098px;height:490px;background:linear-gradient(90deg,#f0f6f6 0%,#f7fafa 60%,#f1f6f6 100%)}
.guide .script{position:absolute;left:105px;top:65px;font-size:56px}
.guide .h2{left:108px;top:135px;line-height:63px;font-size:46px}
.doc{position:absolute;border-radius:3px;box-shadow:0 6px 18px rgba(0,0,0,.12)}

/* signup */
.signup{top:3588px;height:250px;background:var(--red)}
.signup h2{position:absolute;left:0;width:1200px;top:60px;text-align:center;font-size:46px;font-weight:700;color:var(--white);letter-spacing:1px}

/* footer */
.footer{top:3838px;height:371px;background:var(--white)}
.footer .brand{color:var(--ink);left:110px;top:62px}
.footer .brand .name{font-size:29px;letter-spacing:3px}
.footer .brand .by{font-size:20px;margin-left:185px;margin-top:14px}
.f-head{position:absolute;top:60px;font-size:19px;font-weight:500}
.f-link{position:absolute;font-size:15px;color:#444}
.divider{position:absolute;left:110px;top:282px;width:978px;border-top:1px solid #dcdcdc}
.social{position:absolute;top:297px;width:44px;height:44px;border-radius:50%;border:1.5px solid var(--red);display:flex;align-items:center;justify-content:center}
.social span{width:10px;height:10px;border-radius:50%;background:var(--red)}
</style>
</head>
<body>

<header class="hero">
  <div class="hero-photo" role="img" aria-label="Photo of a muscular man standing in a dark gym with a neon sign"></div>
  <div class="brand" style="left:110px;top:34px">
    <div class="name">VENTURE BRIGHTPATH</div>
    <div class="by">by Marlon Tibbet</div>
  </div>
  <div class="account">
    <svg width="13" height="14" viewBox="0 0 13 14"><circle cx="6.5" cy="4" r="3.5" fill="#fff"/><path d="M0 14c0-4 3-6 6.5-6S13 10 13 14z" fill="#fff"/></svg>
    Register / &nbsp;Login
  </div>
  <nav class="nav"><span>About Us</span><span>Plans</span><span>Why Health and Wellness</span></nav>
  <div class="btn" style="left:960px;top:50px;width:128px;height:51px">Contact</div>
  <div class="script">I am a</div>
  <h1>HEALTH AND<br>WELLNESS GURU</h1>
  <div class="btn" style="left:111px;top:413px;width:234px;height:61px">Make an enquiry</div>
</header>

<section class="about">
  <div class="about-glow"></div>
  <div class="about-photo" role="img" aria-label="Photo of a man running along a waterfront"></div>
  <div class="about-word">A<br>B<br>O<br>U<br>T</div>
  <div class="script">Hello I'm</div>
  <h2>MARLON TIBBET</h2>
  <p class="para" style="left:586px;top:226px;width:508px">Lorem ipsum dolor sit amet, consectetur adipiscing elit, sed do eiusm od tempor incididunt ut labore et dolore magna aliqua. Ut enim admin im veniam, quis nostrud exercitation ullamco laboris nisi ut aliquip ex ea commodo consequat. Duis aute irure dolor in reprehenderit in volu ptate velit esse cillum dolore . Nemo enim ipsam voluptatem quia voluptas sit aspernatur aut odit aut fugit, sed quia consequuntur magni dolores eos qui ratione voluptat.</p>
  <div class="btn" style="left:586px;top:459px;width:228px;height:51px;text-transform:none">@MARLON_TIBBET</div>
</section>

<section class="courses">
  <div class="script">Courses</div>
  <h2 class="h2" style="left:0;width:1200px;text-align:center;top:115px">My daily workout plans</h2>
  <div class="cards">
    <div class="connector"></div>
    <div class="card" style="left:0">
      <svg width="64" height="64" viewBox="0 0 64 64"><circle cx="32" cy="32" r="13" fill="#d9473a"/><g stroke="#d9473a" stroke-width="3" stroke-linecap="round"><line x1="32" y1="2" x2="32" y2="12"/><line x1="32" y1="52" x2="32" y2="62"/><line x1="2" y1="32" x2="12" y2="32"/><line x1="52" y1="32" x2="62" y2="32"/><line x1="11" y1="11" x2="18" y2="18"/><line x1="46" y1="46" x2="53" y2="53"/><line x1="53" y1="11" x2="46" y2="18"/><line x1="18" y1="46" x2="11" y2="53"/></g></svg>
      Exsposure<br>to sunlight</div>
    <div class="card" style="left:199px">
      <svg width="64" height="64" viewBox="0 0 64 64" fill="none" stroke="#d9473a" stroke-width="2.5" stroke-linecap="round"><line x1="32" y1="8" x2="32" y2="30"/><line x1="22" y1="13" x2="42" y2="25"/><line x1="42" y1="13" x2="22" y2="25"/><path d="M4 38q7-6 14 0t14 0 14 0 14 0"/><path d="M4 47q7-6 14 0t14 0 14 0 14 0"/><path d="M4 56q7-6 14 0t14 0 14 0 14 0"/></svg>
      <span style="margin-bottom:20px">Ice bath</span></div>
    <div class="card active" style="left:398px">
      <svg width="64" height="64" viewBox="0 0 64 64" fill="none" stroke="#fff" stroke-width="4" stroke-linecap="round" stroke-linejoin="round"><path d="M8 30h16M4 40h14M12 50h12"/><path d="M30 12l26 0-12 18 14 10-24 18 8-18-12-8z"/></svg>
      Daily<br>movement</div>
    <div class="card" style="left:597px">
      <svg width="64" height="64" viewBox="0 0 64 64" fill="none" stroke="#d9473a" stroke-width="3" stroke-linecap="round"><path d="M10 20v26h22v14"/><path d="M10 46h30"/><path d="M40 6q-6 8 0 16t0 16"/><path d="M52 6q-6 8 0 16t0 16"/></svg>
      <span style="margin-bottom:20px">Sauna</span></div>
    <div class="card" style="left:796px">
      <svg width="64" height="64" viewBox="0 0 64 64"><circle cx="22" cy="22" r="8" fill="#d9473a"/><circle cx="36" cy="18" r="7" fill="#d9473a"/><circle cx="48" cy="24" r="7" fill="#d9473a"/><path d="M4 30h56q-2 24-28 24T4 30z" fill="#d9473a"/><path d="M12 38h40" stroke="#fff" stroke-width="2.5"/></svg>
      Healthy<br>Eating</div>
  </div>
  <div class="plan-title">Daily Movement Plan</div>
  <p class="para" style="left:111px;top:541px;width:470px">Nemo enim ipsam voluptatem quia voluptas sit aspernatur aut odit aut fugit, sed quia consequuntur magni dolores eos qui ratio ne voluptatem sequi nesciunt. Neque porro quisquam est, qui do lorem ipsum quia dolor sit amet, consectetur, adipisci velit, sed quia non numquam eius modi tempora incidunt ut labore et dolore magnam aliquam quaerat voluptatem.</p>
  <div class="btn" style="left:111px;top:752px;width:139px;height:50px;font-size:16px">Buy now</div>
  <div class="shot-glow"></div>
  <div class="shot" style="left:614px;top:484px;width:176px;height:161px;background:linear-gradient(160deg,#3a3a3c,#6d6d70 60%,#2b2b2d)" role="img" aria-label="Photo of a boxing training session in a gym"></div>
  <div class="shot" style="left:614px;top:660px;width:176px;height:194px;background:linear-gradient(160deg,#8a8a8c,#4a4a4c 55%,#1f1f21)" role="img" aria-label="Photo of a man lifting a dumbbell"></div>
  <div class="shot" style="left:807px;top:501px;width:282px;height:337px;background:linear-gradient(160deg,#5b5b5d,#2a2a2c 55%,#161618)" role="img" aria-label="Black and white photo of a man with a chain around his neck in a gym"></div>
</section>

<section class="benefits">
  <div class="benefit-photo" role="img" aria-label="Photo of an older couple jogging together in a park"></div>
  <div class="script">Benefits</div>
  <h2 class="h2">Why health &amp; wellness<br>is important</h2>
  <p class="para" style="left:573px;top:277px;width:515px">Lorem ipsum dolor sit amet, consectetur adipiscing elit, sed do eiusm od tempor incididunt ut labore et dolore magna aliqua.</p>
  <div class="acc open" style="top:366px">Physical health
    <svg width="14" height="9" viewBox="0 0 14 9"><path d="M1 8l6-6 6 6" fill="none" stroke="#fff" stroke-width="2"/></svg></div>
  <p class="para" style="left:607px;top:434px;width:460px;line-height:26px;color:#333">Ut enim ad minima veniam, quis nostrum exercitationem ullam corporis suscipit laboriosam, nisi ut aliquid ex ea commodi con sequatur enderit qui in ea volu.</p>
  <div class="acc" style="top:538px">Mental health
    <svg width="14" height="9" viewBox="0 0 14 9"><path d="M1 1l6 6 6-6" fill="none" stroke="#333" stroke-width="2"/></svg></div>
  <div class="acc" style="top:606px">Social health
    <svg width="14" height="9" viewBox="0 0 14 9"><path d="M1 1l6 6 6-6" fill="none" stroke="#333" stroke-width="2"/></svg></div>
  <div class="acc" style="top:672px">Lifestyle
    <svg width="14" height="9" viewBox="0 0 14 9"><path d="M1 1l6 6 6-6" fill="none" stroke="#333" stroke-width="2"/></svg></div>
</section>

<section class="guide">
  <div class="script">Guide</div>
  <h2 class="h2">My day and a guide to a<br>healthy lifestyle</h2>
  <div class="btn" style="left:108px;top:294px;width:197px;height:51px;font-size:16px">Download PDF</div>
  <div class="doc" style="left:935px;top:42px;width:178px;height:140px;background:linear-gradient(180deg,#7b99b5,#b9a48d)" role="img" aria-label="Photo of a man running by the water"></div>
  <div class="doc" style="left:790px;top:95px;width:160px;height:230px;background:#fbfbfb;transform:rotate(4deg)" role="img" aria-label="Guide page with a sleep chart"></div>
  <div class="doc" style="left:935px;top:180px;width:200px;height:240px;background:#f6f6f6;transform:rotate(12deg)" role="img" aria-label="Guide page with a daily schedule"></div>
  <div class="doc" style="left:690px;top:200px;width:245px;height:245px;background:linear-gradient(160deg,#c44a3a,#e3a34a 40%,#7da24a 70%,#f4f4f4 71%);transform:rotate(-12deg)" role="img" aria-label="Guide page with a photo of healthy food"></div>
</section>

<section class="signup">
  <h2>SIGN UP FOR EXCLUSIVE CONTENT</h2>
  <div class="btn" style="left:522px;top:140px;width:156px;height:50px;font-size:16px">Register</div>
</section>

<footer class="footer">
  <div class="brand">
    <div class="name">VENTURE BRIGHTPATH</div>
    <div class="by">by Marlon Tibbet</div>
  </div>
  <div class="f-head" style="left:603px">Quick links</div>
  <div class="f-link" style="left:603px;top:107px">Home</div>
  <div class="f-link" style="left:603px;top:134px">About Us</div>
  <div class="f-link" style="left:603px;top:161px">Plans</div>
  <div class="f-link" style="left:603px;top:188px">Why Health and Wellness</div>
  <div class="f-link" style="left:603px;top:215px">Contact</div>
  <div class="f-head" style="left:844px">Contact Us</div>
  <div class="f-link" style="left:844px;top:107px;display:flex;align-items:center;gap:8px">
    <svg width="13" height="13" viewBox="0 0 24 24"><path d="M6.6 10.8a15 15 0 006.6 6.6l2.2-2.2c.3-.3.7-.4 1-.2 1.1.4 2.3.6 3.6.6.6 0 1 .4 1 1V20c0 .6-.4 1-1 1A17 17 0 013 4c0-.6.4-1 1-1h3.5c.6 0 1 .4 1 1 0 1.3.2 2.5.6 3.6.1.3 0 .7-.2 1z" fill="#d9473a"/></svg>1 888 555 0142</div>
  <div class="f-link" style="left:844px;top:161px;display:flex;align-items:center;gap:8px">
    <svg width="14" height="11" viewBox="0 0 14 11"><rect width="14" height="11" rx="1" fill="#d9473a"/><path d="M1 1l6 5 6-5" fill="none" stroke="#fff" stroke-width="1.4"/></svg>info@marlontibbet.com</div>
  <div class="divider"></div>
  <div class="f-link" style="left:110px;top:311px;font-size:14px">© Venture Brightpath. All rights reserved.</div>
  <div class="social" style="left:940px"><span></span></div>
  <div class="social" style="left:992px"><span></span></div>
  <div class="social" style="left:1044px"><span></span></div>
</footer>

</body>
</html>
```